Varlow Business Partners
Business Cards & Stationery
Professional
Thomas E. Varlow
CEO
58 Birch Lane, North
Suite 318
Edgeton, NJ 07415
thomas.varlow@varlowbp.com
Back of card should contain the black version of the logo - no other information

```html
<!DOCTYPE html>
<html lang="en">
<head>
<meta charset="utf-8">
<title>Varlow Business Partners – Business Cards</title>
<link rel="stylesheet" href="https://fonts.googleapis.com/css2?family=Open+Sans:wght@400;600;700&display=swap">
<style>
  :root {
    --board: #e6e6e6;
    --paper: #ffffff;
    --ink: #333333;
    --grey: #8a8a8a;
    --orange: #f26522;
    --black: #000000;
    --white: #ffffff;
  }
  * { margin: 0; padding: 0; box-sizing: border-box; }
  html, body { width: 1200px; height: 732px; overflow: hidden; }
  body {
    background: var(--board);
    font-family: "Open Sans", Arial, sans-serif;
    position: relative;
  }
  .card {
    position: absolute;
    width: 552px;
    height: 288px;
    overflow: hidden;
    box-shadow: 0 3px 10px rgba(0,0,0,0.18);
  }
  .card--front { left: 24px; top: 247px; width: 533px; height: 286px; background: var(--paper); }
  .card--back { left: 629px; top: 48px; width: 549px; height: 288px; background: var(--black); }
  .card--plain {
    left: 612px; top: 384px;
    background: var(--paper);
    transform: rotate(-12deg);
  }

  .holder { position: absolute; left: 65px; top: 36px; }
  .holder__name { font-size: 17px; font-weight: 700; color: var(--ink); }
  .holder__title { font-size: 15px; font-weight: 600; color: var(--orange); margin-top: 4px; }

  .wave { position: absolute; left: 0; bottom: 0; width: 100%; height: 170px; }

  .contact {
    position: absolute; left: 65px; top: 168px;
    list-style: none;
    font-size: 11.5px; line-height: 15.5px;
    color: var(--white);
  }

  .brand { position: absolute; display: flex; align-items: center; gap: 14px; }
  .brand__dot { border-radius: 50%; background: var(--orange); flex: none; }
  .brand__name {
    font-weight: 600; text-transform: uppercase; line-height: 1.05; letter-spacing: 0.5px;
  }
  .card--front .brand { left: 318px; top: 46px; gap: 10px; }
  .card--front .brand__dot { width: 22px; height: 22px; }
  .card--front .brand__name { font-size: 14px; color: var(--grey); }

  .card--back .brand { left: 90px; top: 96px; }
  .card--back .brand__dot { width: 40px; height: 40px; }
  .card--back .brand__name { font-size: 30px; color: var(--white); }

  .card--plain .brand { left: 90px; top: 96px; }
  .card--plain .brand__dot { width: 40px; height: 40px; }
  .card--plain .brand__name { font-size: 30px; color: var(--grey); }
</style>
</head>
<body>

  <section class="card card--front" aria-label="Business card, front">
    <div class="holder">
      <p class="holder__name">Thomas E. Varlow</p>
      <p class="holder__title">CEO</p>
    </div>

    <div class="brand">
      <span class="brand__dot"></span>
      <p class="brand__name">Varlow<br>Business<br>Partners</p>
    </div>

    <svg class="wave" viewBox="0 0 533 170" preserveAspectRatio="none" aria-hidden="true">
      <path d="M0 30 C120 10 220 60 330 55 C420 50 480 20 533 10 L533 170 L0 170 Z" fill="var(--black)"/>
      <path d="M0 38 C120 20 220 70 330 65 C420 60 480 30 533 22 L533 170 L0 170 Z" fill="var(--orange)"/>
    </svg>

    <ul class="contact">
      <li>58 Birch Lane, North</li>
      <li>Suite 318</li>
      <li>Edgeton, NJ 07415</li>
      <li>Phone: 555.204.6183</li>
      <li>Email: thomas.varlow@varlowbp.com</li>
    </ul>
  </section>

  <section class="card card--back" aria-label="Business card, back">
    <div class="brand">
      <span class="brand__dot"></span>
      <p class="brand__name">Varlow<br>Business Partners</p>
    </div>
  </section>

  <section class="card card--plain" aria-label="Business card, white back">
    <div class="brand">
      <span class="brand__dot"></span>
      <p class="brand__name">Varlow<br>Business Partners</p>
    </div>
  </section>

</body>
</html>
```